landscaping core flute signs

I need core flutes created with business name and a few extra dot points for putting on fences for job sites 120cm x 120cm approx.
I want our old ones information with the new L logo and colour palette

```html
<!DOCTYPE html>
<html lang="en">
<head>
<meta charset="utf-8">
<title>Keystone Earth – Site Sign</title>
<link href="https://fonts.googleapis.com/css2?family=Poppins:wght@500;700;800&display=swap" rel="stylesheet">
<style>
  :root {
    --backdrop: #d4d4d4;
    --sign-white: #ffffff;
    --ink: #0b0b0b;
    --leaf-green: #5f8f4e;
    --mist: #f3f3f3;
    --divider: #e2e2e2;
  }
  * { box-sizing: border-box; margin: 0; padding: 0; }
  html, body {
    width: 705px; height: 1200px; overflow: hidden;
    background: var(--backdrop);
  }
  .sign {
    position: absolute; left: 22px; top: 270px;
    width: 660px; height: 660px;
    background: var(--sign-white);
    box-shadow: 8px 10px 18px rgba(0,0,0,.28);
    overflow: hidden;
  }
  .sign__decor {
    position: absolute; top: 0; width: 200px; height: 200px;
    background: radial-gradient(ellipse at 50% 30%, var(--mist) 0%, rgba(243,243,243,0) 75%);
  }
  .sign__decor--left { left: 4px; border-top-left-radius: 18px; }
  .sign__decor--right { right: 4px; border-top-right-radius: 18px; }

  .brand {
    position: absolute; top: 28px; left: 0; right: 0;
    text-align: center;
  }
  .brand__dot {
    width: 140px; height: 140px; border-radius: 50%;
    background: var(--leaf-green);
    margin: 0 auto 22px;
  }
  .brand__name {
    font-family: "Poppins", sans-serif; font-weight: 700;
    color: var(--ink); font-size: 40px; line-height: 1;
    letter-spacing: 1px;
  }

  .services {
    position: absolute; top: 305px; left: 38px; right: 38px;
    display: flex; justify-content: space-between;
  }
  .service { flex: 1; text-align: center; position: relative; }
  .service + .service::before {
    content: ""; position: absolute; left: 0; top: -6px;
    width: 2px; height: 150px; background: var(--divider);
  }
  .service__icon { display: block; margin: 0 auto 8px; }
  .service__label {
    font-family: "Poppins", sans-serif; font-weight: 800;
    font-size: 19px; line-height: 1.2; color: var(--ink);
    letter-spacing: -.3px;
  }

  .contact {
    position: absolute; left: 0; right: 0; bottom: 0; height: 184px;
    background: var(--ink); color: var(--sign-white);
    text-align: center; padding-top: 16px;
  }
  .contact__phone {
    display: flex; align-items: center; justify-content: center; gap: 12px;
    font-family: "Poppins", sans-serif; font-weight: 700;
    font-size: 66px; line-height: 1; letter-spacing: 1px;
  }
  .contact__email {
    display: flex; align-items: center; justify-content: center; gap: 10px;
    margin-top: 4px;
    font-family: "Poppins", sans-serif; font-weight: 500;
    font-size: 30px; letter-spacing: 1px;
  }
  .contact__licence {
    display: inline-block; margin-top: 6px;
    border: 1.5px solid var(--leaf-green); border-radius: 16px;
    padding: 2px 12px;
    font-family: "Poppins", sans-serif; font-weight: 500;
    font-size: 14px; letter-spacing: 2px;
  }
</style>
</head>
<body>
  <main class="sign">
    <div class="sign__decor sign__decor--left" role="img" aria-label="Faint leaf decoration"></div>
    <div class="sign__decor sign__decor--right" role="img" aria-label="Faint leaf decoration"></div>

    <header class="brand">
      <div class="brand__dot"></div>
      <h1 class="brand__name">KEYSTONE EARTH</h1>
    </header>

    <section class="services">
      <div class="service">
        <svg class="service__icon" width="84" height="80" viewBox="0 0 84 80" role="img" aria-label="Paving icon">
          <path d="M4 42 A38 38 0 0 1 80 42" fill="none" stroke="#0b0b0b" stroke-width="2"/>
          <circle cx="42" cy="44" r="34" fill="#5f8f4e"/>
        </svg>
        <p class="service__label">PAVING &amp;<br>CONCRETING</p>
      </div>
      <div class="service">
        <svg class="service__icon" width="84" height="80" viewBox="0 0 84 80" role="img" aria-label="Garden design icon">
          <path d="M4 42 A38 38 0 0 1 80 42" fill="none" stroke="#0b0b0b" stroke-width="2"/>
          <circle cx="42" cy="44" r="34" fill="#5f8f4e"/>
        </svg>
        <p class="service__label">DESIGN &amp;<br>CONSTRUCTION</p>
      </div>
      <div class="service">
        <svg class="service__icon" width="84" height="80" viewBox="0 0 84 80" role="img" aria-label="Fencing icon">
          <path d="M4 42 A38 38 0 0 1 80 42" fill="none" stroke="#0b0b0b" stroke-width="2"/>
          <circle cx="42" cy="44" r="34" fill="#5f8f4e"/>
        </svg>
        <p class="service__label">FENCING &amp;<br>RETAINING</p>
      </div>
    </section>

    <footer class="contact">
      <div class="contact__phone">
        <svg width="54" height="54" viewBox="0 0 54 54" aria-hidden="true">
          <circle cx="27" cy="27" r="27" fill="#5f8f4e"/>
          <path d="M18 14c2-1 4 0 5 2l2 5c1 2 0 3-1 4l-2 1c1 4 5 8 9 9l1-2c1-1 2-2 4-1l5 2c2 1 3 3 2 5l-1 2c-1 2-3 3-6 3-11-1-20-10-21-21 0-3 1-5 3-6z" fill="#fff"/>
          <path d="M30 14a10 10 0 0 1 10 10M30 19a5 5 0 0 1 5 5" fill="none" stroke="#fff" stroke-width="2.4" stroke-linecap="round"/>
        </svg>
        <span>0412 555 018</span>
      </div>
      <div class="contact__email">
        <svg width="24" height="16" viewBox="0 0 24 16" aria-hidden="true">
          <rect x="0" y="0" width="24" height="16" fill="#5f8f4e"/>
          <path d="M1 1l11 8 11-8M1 15l8-7M23 15l-8-7" fill="none" stroke="#0b0b0b" stroke-width="1.6"/>
        </svg>
        <span>jordan@keystoneearth.com</span>
      </div>
      <span class="contact__licence">QBSA: 1048273</span>
    </footer>
  </main>
</body>
</html>
```